Tri-fold Brochure Design for Banking Business

The brochure we have needs to be improved - more business like and more attractive. Logo file and brochure is attached. I would like to be able to edit the text after you get done. Your ideas and changes to text are welcome. See our website www.korvanbridgegrp.com for our theme. We can use indesign to edit the text after you complete. However, please make changes to the text we have in the design that it uploaded. Your comments and changes are welcome.

Target Market(s)

Human Resources and learning & development staff at the global investment banks - Pellham Trask, QWNR, etc.

Industry/Entity Type

Investment Banking

Logo Text

Korvan Bridge Group

Font styles to use
Serif
Sans Serif

Colors
33a6d7
0493ce
3277b5
fbf289
fdf9cf
fbee3e
0555a3
85acd3

Requirements
Must have
• Must be similar to our website www.korvanbridgegrp.com. Needs to be business-like, clean fonts, sharp design. Our logo - of course.
Nice to have
• City images - seems to be our theme.

```html
<!DOCTYPE html>
<html lang="en">
<head>
<meta charset="utf-8">
<title>Korvan Bridge Group – Tri-fold Brochure</title>
<link rel="stylesheet" href="https://fonts.googleapis.com/css2?family=Exo+2:wght@600;700&family=Roboto+Condensed:wght@400&family=Roboto:wght@400;700&display=swap">
<style>
  :root {
    --page-bg: #e9eaec;
    --brand-blue: #1f73d3;
    --brand-blue-deep: #0555a3;
    --accent-yellow: #f2d42a;
    --ink: #1b1b1b;
    --ink-soft: #2b2b2b;
    --paper: #ffffff;
    --map-grey: #6b6b6b;
  }
  * { box-sizing: border-box; margin: 0; padding: 0; }
  html, body { width: 960px; height: 1200px; overflow: hidden; }
  body { background: var(--page-bg); font-family: "Roboto", Arial, sans-serif; }

  .brochure {
    position: absolute; left: 30px; top: 282px;
    width: 900px; height: 637px;
    display: flex;
    box-shadow: 0 6px 18px rgba(0,0,0,0.25);
  }
  .panel { position: relative; width: 300px; height: 100%; overflow: hidden; }

  /* About panel */
  .panel--about { background: var(--paper); }
  .tab {
    position: absolute; left: 0; top: 33px;
    height: 30px; width: 125px;
    background: var(--accent-yellow);
    clip-path: polygon(0 0, 88% 0, 100% 100%, 0 100%);
    font-family: "Exo 2", sans-serif; font-weight: 700;
    font-size: 15px; color: var(--ink);
    padding: 6px 0 0 19px; letter-spacing: 0.2px;
  }
  .about-copy {
    position: absolute; left: 18px; top: 80px; width: 265px;
    font-family: "Roboto Condensed", sans-serif; font-size: 11.6px;
    line-height: 13px; color: var(--ink-soft); text-align: justify;
  }
  .about-copy p + p { margin-top: 12px; }
  .photo-about {
    position: absolute; left: 0; top: 198px; width: 300px; height: 439px;
    background:
      linear-gradient(180deg, #ffffff 0%, rgba(255,255,255,0) 18%),
      linear-gradient(180deg, #dfe3e6 0%, #c9ced2 35%, #6f7f90 62%, #3a4e66 80%, #2a3446 100%);
  }

  /* Contact panel */
  .panel--contact { background: linear-gradient(180deg, var(--brand-blue) 0%, #2477d6 55%, var(--brand-blue) 100%); }
  .contact-title {
    position: absolute; left: 87px; top: 119px; width: 125px; height: 26px;
    background: var(--accent-yellow);
    font-family: "Exo 2", sans-serif; font-weight: 600; font-size: 14.5px;
    color: var(--ink); text-align: center; line-height: 26px;
  }
  .office {
    position: absolute; left: 53px; width: 194px; height: 36px;
    border: 1px solid #ffffff; text-align: center;
    padding-top: 3px;
  }
  .office__region { font-weight: 700; font-size: 11px; color: var(--accent-yellow); line-height: 14px; }
  .office__email { font-size: 10.5px; color: #ffffff; line-height: 14px; }
  .globe { position: absolute; left: 140px; top: 372px; width: 20px; height: 20px; }
  .contact-web {
    position: absolute; left: 0; top: 397px; width: 300px; text-align: center;
    font-weight: 700; font-size: 10.5px; color: #ffffff;
  }
  .map-card {
    position: absolute; left: 17px; top: 436px; width: 268px; height: 178px;
    background: var(--paper); border-radius: 14px;
  }
  .world-map {
    position: absolute; left: 13px; top: 18px; width: 242px; height: 130px;
    background: radial-gradient(ellipse at center, #7a7a7a 0%, var(--map-grey) 55%, #d6d6d6 100%);
    border-radius: 40px;
  }
  .map-caption {
    position: absolute; left: 0; bottom: 10px; width: 100%; text-align: center;
    font-weight: 700; font-size: 10.5px; color: var(--ink);
  }

  /* Cover panel */
  .panel--cover { background: linear-gradient(180deg, #eef3f8 0%, #dbe6f0 100%); }
  .brand {
    position: absolute; left: 0; top: 36px; width: 100%;
    display: flex; justify-content: center; align-items: center; gap: 8px;
  }
  .brand__mark { width: 22px; height: 22px; background: var(--brand-blue); }
  .brand__name {
    font-family: "Exo 2", sans-serif; font-weight: 700; font-size: 19px;
    color: var(--ink); letter-spacing: 0.3px;
  }
  .cover-title {
    position: absolute; left: 0; top: 112px; width: 100%; text-align: center;
    font-family: "Exo 2", sans-serif; font-weight: 700; font-size: 17px;
    line-height: 24px; color: var(--ink);
  }
  .photo-cover {
    position: absolute; left: 0; top: 168px; width: 300px; height: 469px;
    background:
      linear-gradient(180deg, #dbe6f0 0%, rgba(219,230,240,0) 16%),
      linear-gradient(180deg, #c9d6e2 0%, #8e9aa6 30%, #6d5a4a 55%, #8a5a3c 72%, #4a4a4e 88%, #5d7286 100%);
  }
  .cover-band {
    position: absolute; left: 0; top: 591px; width: 300px; height: 23px;
    background: var(--accent-yellow);
    font-weight: 700; font-size: 10.5px; letter-spacing: 2.6px;
    color: var(--ink); text-align: center; line-height: 23px;
  }
</style>
</head>
<body>
  <div class="brochure">
    <section class="panel panel--about">
      <h2 class="tab">ABOUT US</h2>
      <div class="about-copy">
        <p>Korvan Bridge Group efficiently provides complete sales, marketing and logistical support for all our programs, no matter the location.</p>
        <p>Our globally located trainers have extensive experience, both as industry professionals and as trainers.</p>
        <p>Our highly qualified logistical team complement the training services, providing reliable and efficient support</p>
      </div>
      <div class="photo-about" role="img" aria-label="City skyline photo: glass tower and riverside buildings at dusk"></div>
    </section>

    <section class="panel panel--contact">
      <h2 class="contact-title">GET IN TOUCH</h2>
      <div class="office" style="top:160px">
        <div class="office__region">GLOBAL:</div>
        <div class="office__email">nadia.verelli@korvanbridgegrp.com</div>
      </div>
      <div class="office" style="top:212px">
        <div class="office__region">ASIA:</div>
        <div class="office__email">owen.tasker@korvanbridgegrp.com</div>
      </div>
      <div class="office" style="top:264px">
        <div class="office__region">UNITED STATES:</div>
        <div class="office__email">paul.renick@korvanbridgegrp.com</div>
      </div>
      <div class="office" style="top:316px">
        <div class="office__region">EUROPE:</div>
        <div class="office__email">lena.marsh@korvanbridgegrp.com</div>
      </div>
      <svg class="globe" viewBox="0 0 20 20" aria-hidden="true">
        <g fill="none" stroke="#f2d42a" stroke-width="1.4">
          <circle cx="10" cy="10" r="8.5"/>
          <ellipse cx="10" cy="10" rx="4" ry="8.5"/>
          <line x1="1.5" y1="10" x2="18.5" y2="10"/>
          <line x1="3" y1="5.5" x2="17" y2="5.5"/>
          <line x1="3" y1="14.5" x2="17" y2="14.5"/>
        </g>
      </svg>
      <div class="contact-web">www.korvanbridgegrp.com</div>
      <div class="map-card">
        <div class="world-map" role="img" aria-label="Grey world map showing the continents"></div>
        <div class="map-caption">Worldwide Training Service</div>
      </div>
    </section>

    <section class="panel panel--cover">
      <div class="brand">
        <span class="brand__mark"></span>
        <span class="brand__name">Korvan Bridge Group</span>
      </div>
      <h1 class="cover-title">YOUR EXPERT TRAINING<br>AND CONSULTING PARTNER</h1>
      <div class="photo-cover" role="img" aria-label="City skyline photo: high-rise towers along a waterfront"></div>
      <div class="cover-band">www.korvanbridgegrp.com</div>
    </section>
  </div>
</body>
</html>
```